Brivel Metrics New Website for Health Benefits Plan Decisioneering Tool Launch

Brivel Metrics is a SaaS provider of health benefits comparison tools. We need a new simple SaaS focused website to direct customers to our product

Target Market(s)

General Public comparing their health benefits plans from their employer or from the state exchanges in the US

Coding

Coded - Design and coding required

Number of Pages Required

3 page

Requirements
Must have
• Main page - "Know the Best Health Benefits Plan for You!"
Graphic of a person looking over papers on their desk
Compare Now button to link to SaaS product
About Us
Product Page

https://plovix.example/top-cloud-sites/

```html
<!DOCTYPE html>
<html lang="en">
<head>
<meta charset="utf-8">
<title>Brivel Metrics LLC – Know the Best Health Benefits Plan for You</title>
<link href="https://fonts.googleapis.com/css2?family=Poppins:wght@400;500;600;700&display=swap" rel="stylesheet">
<style>
:root{
  --blue:#1e9bd7;
  --blue-soft:#e3f1fb;
  --ink:#15172b;
  --text:#555a6b;
  --muted:#8a8f9c;
  --line:#e4e7ee;
  --card:#ffffff;
  --wash:#f6f8fd;
  --teal:#5cbfb4;
  --pink:#f0687f;
  --orange:#f7a274;
  --green:#9fd06b;
}
*{margin:0;padding:0;box-sizing:border-box}
html,body{width:1200px;height:5004px;overflow:hidden;background:#fff}
body{position:relative;font-family:"Poppins",sans-serif;color:var(--ink)}
.abs{position:absolute}
.label{position:absolute;font-size:17px;font-weight:600;color:var(--blue);letter-spacing:.5px;text-transform:uppercase}
.h2{position:absolute;font-size:38px;font-weight:600;color:var(--ink);line-height:1.2}
.center{left:0;width:1200px;text-align:center}
.btn{position:absolute;background:var(--blue);color:#fff;border-radius:26px;font-size:15px;font-weight:500;display:flex;align-items:center;justify-content:center;box-shadow:0 8px 18px rgba(30,155,215,.25)}
.bar{position:absolute;height:4px;width:52px;background:var(--blue);border-radius:2px}

/* header */
.brand{position:absolute;left:112px;top:28px;color:var(--blue);font-size:32px;font-weight:500;letter-spacing:1px;line-height:1}
.brand small{display:block;font-size:16px;letter-spacing:4px;margin-top:4px;text-align:center;border-top:2px solid var(--blue);padding-top:2px;width:170px;margin-left:60px}
.nav{position:absolute;top:40px;left:610px;display:flex;gap:28px;font-size:15px;font-weight:500;color:var(--ink)}
.nav .on{color:var(--blue)}
.hero-wave{position:absolute;left:0;top:0;width:640px;height:530px;background:linear-gradient(120deg,#fafafa 0%,#f1f1f3 45%,#fff 100%)}
.hero-art{position:absolute;left:588px;top:97px;width:612px;height:433px;background:linear-gradient(180deg,#d9e6f2 0%,#c2cde6 55%,#b6763f 100%)}
.hero-title{position:absolute;left:112px;top:192px;font-size:40px;font-weight:600;line-height:1.22;color:var(--ink)}

/* products */
.blob{position:absolute;background:var(--blue-soft);border-radius:50%}
.pcard{position:absolute;width:299px;height:336px;background:var(--card);box-shadow:0 4px 24px rgba(20,30,60,.08);text-align:center}
.pcard .ic{position:absolute;left:108px;top:57px;width:84px;height:84px;border-radius:50%}
.pcard h3{position:absolute;top:188px;left:0;width:100%;font-size:16px;font-weight:600}
.pcard p{position:absolute;top:222px;left:28px;right:28px;font-size:13.5px;line-height:25px;color:var(--text)}
.pcard svg.arr{position:absolute;left:133px;top:290px}

/* values */
.vcard{position:absolute;width:235px;height:222px;background:var(--card);box-shadow:0 4px 20px rgba(20,30,60,.08);text-align:center}
.vcard .ic{position:absolute;left:85px;top:20px;width:64px;height:64px;border-radius:50%;border:2px solid #c8d7ec;display:flex;align-items:center;justify-content:center}
.vcard h4{position:absolute;top:94px;width:100%;font-size:16px;font-weight:500}
.vcard p{position:absolute;top:126px;left:16px;right:16px;font-size:13px;line-height:27px;color:var(--text)}
.vcard a{position:absolute;top:182px;left:0;width:100%;font-size:14px;color:var(--blue);text-decoration:none;font-weight:500}

/* testimonials */
.tcard{position:absolute;top:2718px;width:334px;height:292px;background:#fff;box-shadow:0 4px 24px rgba(20,30,60,.1);padding:38px 22px}
.tcard .co{font-size:22px;font-weight:500;color:#444}
.tcard p{margin-top:22px;font-size:14px;line-height:31px;color:var(--text)}
.tcard .who{margin-top:22px;font-size:17px;font-weight:600}
.tcard .role{font-size:13px;color:var(--text)}
.tcard .q{position:absolute;right:20px;bottom:38px;font-size:96px;line-height:.6;color:#dcdfe4;font-weight:700}

/* partners */
.partner{position:absolute;top:3226px;font-size:34px;font-weight:500;color:#3b3f4a;display:flex;align-items:center;gap:10px}
.partner i{display:inline-block;width:26px;height:26px;border:2px solid #3b3f4a;border-radius:4px}

/* contact */
.form{position:absolute;left:111px;top:3553px;width:458px;height:491px;background:#fff;box-shadow:0 4px 26px rgba(20,30,60,.09)}
.field{position:absolute;left:56px;width:360px;font-size:14px;color:var(--text);border-bottom:1px solid var(--line)}

/* newsletter */
.news-in{position:absolute;left:301px;top:4454px;width:598px;height:56px;border:1px solid var(--line);border-radius:28px;box-shadow:0 6px 20px rgba(20,30,60,.07);font-size:14px;color:var(--text);padding:18px 20px;background:#fff}
.news-btn{position:absolute;left:823px;top:4454px;width:76px;height:56px;background:var(--blue);border-radius:0 28px 28px 0;display:flex;align-items:center;justify-content:center}

/* footer */
.fcol{position:absolute;top:4716px;font-size:14px;color:#2a2d3a}
.fcol h5{font-size:17px;font-weight:600;margin-bottom:10px}
.fcol li{list-style:none;line-height:31px}
.social{position:absolute;top:4850px;width:38px;height:38px;border-radius:50%}
</style>
</head>
<body>

<!-- Hero -->
<div class="hero-wave" role="img" aria-label="Soft grey wave-mesh background pattern"></div>
<div class="hero-art" role="img" aria-label="Illustration of a man at his desk reviewing papers while on the phone, with a laptop and stacked binders"></div>
<div class="brand">BRIVEL METRICS<small>LLC</small></div>
<nav class="nav"><span class="on">Home</span><span>Services</span><span>Resorces</span><span>Blog</span><span>Insights</span><span>Contact Us</span></nav>
<h1 class="hero-title">Know the Best Health<br>Benefits Plan for You!</h1>
<div class="btn" style="left:112px;top:305px;width:131px;height:46px">Get Started</div>
<svg class="abs" style="left:190px;top:415px" width="90" height="90" viewBox="0 0 90 90">
  <circle cx="45" cy="45" r="43" fill="#fff" stroke="#bfe1f3" stroke-width="2"/>
  <circle cx="45" cy="45" r="34" fill="#fff" stroke="var(--blue)" stroke-width="2"/>
  <path d="M39 35 L55 45 L39 55 Z" fill="var(--blue)"/>
</svg>
<svg class="abs" style="left:544px;top:521px" width="50" height="50" viewBox="0 0 50 50">
  <circle cx="25" cy="25" r="24" fill="#fff" stroke="#e2e4ea"/>
  <path d="M16 21 L25 30 L34 21" fill="none" stroke="#444" stroke-width="2"/>
</svg>

<!-- About -->
<div class="abs" style="left:39px;top:650px;width:496px;height:330px;border-radius:20px;background:radial-gradient(circle at 50% 50%,#e8f3fb 0%,#f3f5f8 55%,#fff 80%)" role="img" aria-label="World map with circular photos of people working, around a central brand circle"></div>
<div class="label" style="left:623px;top:660px">About Us</div>
<div class="h2" style="left:619px;top:690px">Brivel Metrics LLC</div>
<div class="bar" style="left:621px;top:755px;width:70px"></div>
<p class="abs" style="left:621px;top:786px;width:470px;font-size:13.5px;line-height:28px;color:var(--text)">Lorem ipsum dolor sit amet, consectetur adipiscing elit, sed do eiusmod tempor incididunt ut labore et dolore magna aliqua. Quis ipsum suspendisse ultrices gravida. Risus commodo viverra maecenas accumsan lacus vel facilisis.</p>
<div class="btn" style="left:614px;top:924px;width:165px;height:50px">Learn More</div>

<!-- Products -->
<div class="blob" style="left:-260px;top:1290px;width:980px;height:760px;border-radius:48% 52% 40% 60%"></div>
<div class="label center" style="top:1082px">Services</div>
<div class="h2 center" style="top:1112px">Our Products</div>

<div class="pcard" style="left:111px;top:1202px"><div class="ic" style="background:var(--teal)"></div><h3>Quis ipsum sus</h3><p>Lorem ipsum dolor sit aconsectetur adipiscing elit, sed do eiusmod</p><svg class="arr" width="34" height="16"><path d="M1 8H32M25 1l7 7-7 7" fill="none" stroke="var(--blue)" stroke-width="2"/></svg></div>
<div class="pcard" style="left:449px;top:1202px"><div class="ic" style="background:var(--pink)"></div><h3>Quis ipsum sus</h3><p>Lorem ipsum dolor sit aconsectetur adipiscing elit, sed do eiusmod</p><svg class="arr" width="34" height="16"><path d="M1 8H32M25 1l7 7-7 7" fill="none" stroke="var(--blue)" stroke-width="2"/></svg></div>
<div class="pcard" style="left:787px;top:1202px"><div class="ic" style="background:var(--teal)"></div><h3>Quis ipsum sus</h3><p>Lorem ipsum dolor sit aconsectetur adipiscing elit, sed do eiusmod</p><svg class="arr" width="34" height="16"><path d="M1 8H32M25 1l7 7-7 7" fill="none" stroke="var(--blue)" stroke-width="2"/></svg></div>
<div class="pcard" style="left:111px;top:1577px"><div class="ic" style="background:var(--orange)"></div><h3>Quis ipsum sus</h3><p>Lorem ipsum dolor sit aconsectetur adipiscing elit, sed do eiusmod</p><svg class="arr" width="34" height="16"><path d="M1 8H32M25 1l7 7-7 7" fill="none" stroke="var(--blue)" stroke-width="2"/></svg></div>
<div class="pcard" style="left:449px;top:1577px"><div class="ic" style="background:var(--teal)"></div><h3>Quis ipsum sus</h3><p>Lorem ipsum dolor sit aconsectetur adipiscing elit, sed do eiusmod</p><svg class="arr" width="34" height="16"><path d="M1 8H32M25 1l7 7-7 7" fill="none" stroke="var(--blue)" stroke-width="2"/></svg></div>
<div class="pcard" style="left:787px;top:1577px"><div class="ic" style="background:var(--green)"></div><h3>Quis ipsum sus</h3><p>Lorem ipsum dolor sit aconsectetur adipiscing elit, sed do eiusmod</p><svg class="arr" width="34" height="16"><path d="M1 8H32M25 1l7 7-7 7" fill="none" stroke="var(--blue)" stroke-width="2"/></svg></div>

<!-- Values -->
<div class="label center" style="top:2093px">Our Valus</div>
<div class="h2 center" style="top:2124px">Value proposition &amp; Benefits</div>

<div class="vcard" style="left:111px;top:2219px"><div class="ic"><svg width="30" height="30"><rect x="6" y="6" width="18" height="18" rx="3" fill="none" stroke="var(--blue)" stroke-width="2"/></svg></div><h4>boutique</h4><p>Lorem ipsum dolor sit amet, consectetur adipiscing elit,</p><a>Raed More</a></div>
<div class="vcard" style="left:357px;top:2246px"><div class="ic"><svg width="30" height="30"><circle cx="15" cy="13" r="8" fill="none" stroke="var(--blue)" stroke-width="2"/><path d="M10 20l-2 8 7-3 7 3-2-8" fill="none" stroke="var(--blue)" stroke-width="2"/></svg></div><h4>Quality</h4><p>Lorem ipsum dolor sit amet, consectetur adipiscing elit,</p><a>Raed More</a></div>
<div class="vcard" style="left:604px;top:2219px"><div class="ic"><svg width="30" height="30"><circle cx="15" cy="12" r="8" fill="none" stroke="var(--blue)" stroke-width="2"/><path d="M15 20v8" stroke="var(--blue)" stroke-width="2"/></svg></div><h4>Flexibility</h4><p>Lorem ipsum dolor sit amet, consectetur adipiscing elit,</p><a>Raed More</a></div>
<div class="vcard" style="left:851px;top:2246px"><div class="ic"><svg width="30" height="30"><path d="M15 3l11 12-11 12L4 15Z" fill="none" stroke="var(--blue)" stroke-width="2"/></svg></div><h4>Problem Solving</h4><p>Lorem ipsum dolor sit amet, consectetur adipiscing elit,</p><a>Raed More</a></div>

<!-- Testimonials -->
<div class="blob" style="left:660px;top:2560px;width:640px;height:520px;border-radius:55% 45% 50% 50%;background:#eef6fc"></div>
<div class="abs" style="left:0;top:2718px;width:160px;height:360px;background:radial-gradient(#d8dbe2 1.4px,transparent 1.6px) 0 0/12px 12px;opacity:.7"></div>
<div class="label" style="left:0;width:466px;text-align:right;top:2766px">Testmonials</div>
<div class="h2" style="left:0;width:446px;text-align:right;top:2810px">Our Customers<br>Feedback.</div>
<div class="abs" style="left:359px;top:2964px;width:28px;height:4px;background:var(--blue);border-radius:2px"></div>
<div class="abs" style="left:400px;top:2960px;width:11px;height:11px;border:1.5px solid #aab;border-radius:50%"></div>
<div class="abs" style="left:421px;top:2960px;width:11px;height:11px;border:1.5px solid #aab;border-radius:50%"></div>

<div class="tcard" style="left:522px"><div class="co">Crewmark</div><p>Lorem ipsum consectetur adipiscing elit, sed do eiusmod tincididunt ut labore et dolore magna aliqua.</p><div class="who">Dana Reyes</div><div class="role">Lorem Ipsum</div><div class="q">”</div></div>
<div class="tcard" style="left:891px"><div class="co">Crewmark</div><p>Lorem ipsum consectetur adipiscing elit, sed do eiusmod tincididunt ut labore et dolore magna aliqua.</p><div class="who">Dana Reyes</div><div class="role">Lorem Ipsum</div><div class="q">”</div></div>

<!-- Partners -->
<div class="partner" style="left:111px">nuvra</div>
<div class="partner" style="left:262px"><i></i>Pathly</div>
<div class="partner" style="left:442px">Crewmark</div>
<div class="partner" style="left:688px">brightloop</div>
<div class="partner" style="left:896px;color:#9aa0ab"><i style="border-color:#9aa0ab"></i>slotwise</div>

<!-- Contact -->
<div class="abs" style="left:0;top:3378px;width:1200px;height:797px;background:linear-gradient(180deg,#fff 0%,var(--wash) 15%,var(--wash) 85%,#fff 100%)"></div>
<div class="form">
  <div class="field" style="top:78px;padding-bottom:16px">Your Email*</div>
  <div class="field" style="top:175px;padding-bottom:16px">Subject*</div>
  <div class="field" style="top:263px;height:90px">Massage*</div>
  <div class="btn" style="left:54px;top:402px;width:165px;height:50px">Send Request</div>
</div>
<div class="label" style="left:716px;top:3594px">Contact Us</div>
<div class="h2" style="left:716px;top:3640px;font-size:37px">Don’t Hesitate to<br>Contact us for any<br>Information.</div>
<div class="bar" style="left:719px;top:3832px"></div>
<div class="abs" style="left:719px;top:3878px;font-size:14.5px;font-weight:500;color:#333">Cal us for immidiate support to this number</div>
<div class="abs" style="left:719px;top:3910px;font-size:20px;font-weight:600">888 888 8888</div>

<!-- Newsletter -->
<svg class="abs" style="left:472px;top:4270px" width="30" height="30"><rect x="7" y="7" width="16" height="16" transform="rotate(20 15 15)" fill="none" stroke="var(--green)" stroke-width="3"/></svg>
<svg class="abs" style="left:26px;top:4440px" width="20" height="20"><circle cx="10" cy="10" r="7" fill="none" stroke="#2aa37b" stroke-width="3"/></svg>
<svg class="abs" style="left:340px;top:4565px" width="36" height="36"><path d="M30 5 L6 18 L30 31 Z" fill="none" stroke="#b9bcc5" stroke-width="2"/></svg>
<div class="h2 center" style="top:4318px;font-size:38px">Subscribe Newsletter &amp; get<br>Company News.</div>
<div class="news-in">Enter your email</div>
<div class="news-btn"><svg width="28" height="28" viewBox="0 0 28 28"><path d="M3 13 L25 3 L18 25 L13 15 Z M13 15 L25 3" fill="none" stroke="#fff" stroke-width="2" stroke-linejoin="round"/></svg></div>

<!-- Footer -->
<div class="brand" style="top:4718px;font-size:26px">BRIVEL METRICS<small style="font-size:13px;width:140px;margin-left:48px">LLC</small></div>
<div class="abs" style="left:112px;top:4778px;font-size:14px;color:#2a2d3a">info@brivelmetricsllc.example</div>
<div class="abs" style="left:112px;top:4810px;font-size:17px;font-weight:500">888 888 8888</div>
<div class="social" style="left:113px;background:var(--blue)"></div>
<div class="social" style="left:163px;border:1px solid var(--line)"></div>
<div class="social" style="left:213px;border:1px solid var(--line)"></div>
<svg class="abs" style="left:38px;top:4915px" width="20" height="20"><path d="M4 4 L16 16 M16 4 L4 16" stroke="#7dbd4a" stroke-width="2"/></svg>

<div class="fcol" style="left:404px"><h5>Services</h5><ul><li>Lorem ipsum dolor sit</li><li>Amet, consectetur adipiscing</li><li>Elit, sed do eiusmod tempor</li><li>Incididunt ut labore et dolore</li><li>Magna aliqua. Quis ipsum</li></ul></div>
<div class="fcol" style="left:709px"><h5>Quick Links</h5><ul><li>About</li><li>Services</li><li>Partner</li><li>Investors &amp; advisors</li></ul></div>
<div class="fcol" style="left:951px"><h5>Company</h5><ul><li>Join us</li><li>Benefits</li><li>Current openings</li></ul></div>
<div class="abs center" style="top:4950px;font-size:14px;color:#2a2d3a">Copyright © 2020. All Rights Reserved</div>

</body>
</html>
```